Business card logo/design needed

I need a new and fresh business card to get my name out there.
I have made plenty before and have a logo but I dont think it is sending the right message across.
I am a personal trainer running a small online business designed to cut the cost of training by taking it online, allowing you to purchase training over the net, through the help of Skype and video uploads.
You can personalized programs hand written for you or more general programs aimed at your goals.
Our goal is to get everyone to look like and behave like an athlete because there is no point in being in shape if you cant do anything with that body.
I also have a strong background in sports, having played low level college basketball in america and worked as a strength and conditioning coach. I dont like running or slow cardio, I am more focused on weights and functional training for aerobic fitness.
I am young for what I do, but I have lot of knowledge and I need something that says that I am not your standard drill sergeant trainer but someone who will truly help you reach your goals.
My curent logo text is "the climb to the top" but I am not set on that.

Industry/Entity Type

Personal Trainer

Contact Information for Business Card

Desmond Quilby
Summit Forge Motion
Personal trainer
Strength and conditioning coach
0481 552 709
www.summitforgemotion.example

```html
<!DOCTYPE html>
<html lang="en">
<head>
<meta charset="utf-8">
<title>Summit Forge Motion – Business Card</title>
<link rel="stylesheet" href="https://fonts.googleapis.com/css2?family=Josefin+Sans:wght@400&family=Mulish:wght@400;700&display=swap">
<style>
  :root {
    --paper: #ffffff;
    --frame: #1a1a1a;
    --card-edge: #3a3a3a;
    --cyan: #00f0ff;
    --blue: #0033ff;
    --red: #ff0000;
  }
  html, body {
    margin: 0;
    padding: 0;
    overflow: hidden;
    background: var(--paper);
  }
  .canvas {
    position: relative;
    width: 1200px;
    height: 1000px;
    box-sizing: border-box;
    border: 2px solid var(--frame);
    background: var(--paper);
    overflow: hidden;
  }
  .card {
    position: absolute;
    left: 214px;
    top: 277px;
    width: 770px;
    height: 444px;
    box-sizing: border-box;
    border: 1px solid var(--card-edge);
    background: var(--paper);
    overflow: hidden;
  }
  .card__graphic {
    position: absolute;
    left: 33px;
    top: 45px;
    width: 188px;
    height: 363px;
    background: linear-gradient(100deg, rgba(0,51,255,0.18), rgba(255,0,0,0.16) 50%, rgba(0,240,255,0.2));
  }
  .brand-name {
    position: absolute;
    left: 259px;
    top: 52px;
    margin: 0;
    font-family: "Josefin Sans", sans-serif;
    font-weight: 400;
    font-size: 40px;
    line-height: 1;
    letter-spacing: -1px;
    color: var(--blue);
    white-space: nowrap;
  }
  .person-name {
    position: absolute;
    left: 259px;
    top: 172px;
    margin: 0;
    font-family: "Josefin Sans", sans-serif;
    font-weight: 400;
    font-size: 31px;
    line-height: 1;
    letter-spacing: 6px;
    white-space: nowrap;
  }
  .person-name__first { color: var(--blue); }
  .person-name__last { color: var(--red); }
  .roles {
    position: absolute;
    left: 259px;
    top: 221px;
    margin: 0;
    font-family: "Mulish", sans-serif;
    font-weight: 400;
    font-size: 20px;
    line-height: 26px;
    color: var(--cyan);
    white-space: nowrap;
  }
  .contact {
    position: absolute;
    left: 259px;
    top: 342px;
    margin: 0;
    font-family: "Mulish", sans-serif;
    font-weight: 700;
    font-size: 21px;
    line-height: 30px;
    color: var(--blue);
    white-space: nowrap;
  }
  .contact span { display: block; }
</style>
</head>
<body>
  <div class="canvas">
    <section class="card">
      <div class="card__graphic" role="img" aria-label="Abstract graphic of crossing thin lines in cyan, blue and red"></div>
      <h1 class="brand-name">SUMMITFORGEMOTION</h1>
      <p class="person-name">
        <span class="person-name__first">Desmond</span>
        <span class="person-name__last">Quilby</span>
      </p>
      <p class="roles">Personal trainer<br>Strength and conditioning coach</p>
      <p class="contact">
        <span class="contact__phone">0481 552 709</span>
        <span class="contact__web">www.summitforgemotion.example</span>
      </p>
    </section>
  </div>
</body>
</html>
```